'Orla Property Development' Business Card

Business Card Features:

High Quality (potentially textured) thick card - preference is white textured card

Logo (supplied)

We plan to use the vertical logo as the main logo. But i am happy for people to use either if they find it works better for the design of the card.

The building icon and also the insert to the 'E' is in a metallic finish, i think this should be finished in a metallic embossed or raised style.
Updates

Please note i have attached both a horizontal and Vertical Logo for your reference. We plan to use the vertical logo as the main logo. But i am happy for people to use either if they find it works better for the design of the card.

Please note i am considering having the cards made on stainless steel. This introduces the option of having cut outs in the card and etching or printing for the design. If you have a good concept for this please submit.

http://www.quorvantprint.co.uk/black-metal-cards# this is a site that makes the metal cards to offer some direction . . . . Please note i am basic the selection o the best design, if that means normal print cards on paper then this is what i will choose. But there are some great options with the metal. Thanks.

Industry/Entity Type

Building

Requirements
Must have
• Helvetica font to details side of card - logo as supplied to opposite side.

Card Details:

Darren Ashcombe
Managing Director

+61 438 615 207
+61 3 8276 4139

PO Box 73
Bentleigh, VIC 3024

darren@orla.properties

www.orla.properties

```html
<!DOCTYPE html>
<html lang="en">
<head>
<meta charset="utf-8">
<title>Orla Property Development – Business Card</title>
<link rel="stylesheet" href="https://fonts.googleapis.com/css2?family=Arimo:wght@400;700&display=swap">
<style>
  :root {
    --page-bg: #e4e4e4;
    --card-black: #1c1c1c;
    --card-black-back: #161616;
    --text-grey: #a8a8a8;
    --name-grey: #8f8f8f;
    --logo-grey: #7d7d7d;
    --rule-grey: #9a9a9a;
    --band-light: #9b9b9b;
    --band-dark: #596061;
    --back-mark: #2e2e2e;
  }
  * { margin: 0; padding: 0; box-sizing: border-box; }
  html, body {
    width: 1200px; height: 720px; overflow: hidden;
    background: var(--page-bg);
    font-family: "Arimo", Helvetica, Arial, sans-serif;
  }
  .card {
    position: absolute; top: 242px;
    width: 420px; height: 239px;
    overflow: hidden;
  }
  .card--front { left: 147px; background: var(--card-black); }
  .card--back { left: 633px; background: var(--card-black-back); }

  /* front */
  .brand {
    position: absolute; left: 20px; top: 24px;
    display: flex; align-items: center; gap: 10px;
    color: var(--logo-grey); font-weight: 700;
  }
  .brand__square { width: 34px; height: 34px; background: var(--logo-grey); }
  .brand__name { font-size: 28px; line-height: 1; letter-spacing: 1px; }
  .brand__sub { display: block; font-size: 7px; letter-spacing: 0.4px; margin-top: 3px; }

  .person {
    position: absolute; right: 17px; top: 102px; text-align: right;
  }
  .person__name { font-size: 13px; font-weight: 700; color: var(--name-grey); }
  .person__title { font-size: 10px; color: var(--text-grey); margin-top: 2px; }

  .rule {
    position: absolute; left: 21px; right: 21px; top: 140px;
    height: 1px; background: var(--rule-grey);
  }

  .contacts {
    position: absolute; left: 21px; top: 155px;
    list-style: none; font-size: 10px; color: var(--text-grey);
  }
  .contacts li { display: flex; align-items: center; gap: 7px; height: 12px; }
  .contacts svg { width: 9px; height: 9px; fill: none; stroke: var(--text-grey); stroke-width: 1.2; }

  .address {
    position: absolute; right: 17px; top: 155px;
    font-size: 10px; line-height: 12px; color: var(--text-grey);
    text-align: right; font-style: normal;
  }

  .band { position: absolute; left: 0; right: 0; bottom: 0; height: 17px; display: flex; }
  .band__light { width: 345px; background: var(--band-light); }
  .band__dark { flex: 1; background: var(--band-dark); }

  /* back */
  .back-brand {
    position: absolute; inset: 0;
    display: flex; flex-direction: column; align-items: center; justify-content: center;
    gap: 10px; color: var(--back-mark); font-weight: 700;
  }
  .back-brand__square { width: 56px; height: 56px; background: var(--back-mark); }
  .back-brand__name { font-size: 44px; line-height: 1; letter-spacing: 2px; }
  .back-brand__sub { font-size: 10px; letter-spacing: 0.5px; }
</style>
</head>
<body>

<section class="card card--front" aria-label="Business card front">
  <div class="brand">
    <span class="brand__square"></span>
    <div>
      <span class="brand__name">ORLA</span>
      <span class="brand__sub">Property Development</span>
    </div>
  </div>

  <div class="person">
    <p class="person__name">Darren Ashcombe</p>
    <p class="person__title">Managing Director</p>
  </div>

  <div class="rule"></div>

  <ul class="contacts">
    <li><svg viewBox="0 0 10 10"><path d="M1 3c0-1 1-2 4-2s4 1 4 2M2 4h6l1 5H1z"/></svg>0438615207</li>
    <li><svg viewBox="0 0 10 10"><rect x="3" y="0.6" width="4" height="8.8" rx="0.8"/></svg>1800 274 318</li>
    <li><svg viewBox="0 0 10 10"><rect x="0.6" y="2" width="8.8" height="6"/><path d="M0.6 2l8.8 6M9.4 2L0.6 8"/></svg>darren@orla.properties</li>
    <li><svg viewBox="0 0 10 10"><rect x="0.6" y="1" width="8.8" height="6"/><path d="M5 7v2M3 9.3h4"/></svg>www.orla.properties</li>
  </ul>

  <address class="address">PO BOX 73 Bentleigh,<br>VIC 3024</address>

  <div class="band"><span class="band__light"></span><span class="band__dark"></span></div>
</section>

<section class="card card--back" aria-label="Business card back">
  <div class="back-brand">
    <span class="back-brand__square"></span>
    <span class="back-brand__name">ORLA</span>
    <span class="back-brand__sub">Property Development</span>
  </div>
</section>

</body>
</html>
```